Control panel UI redesign for a learning simulation

Hello. I'm producing a learning simulation and need help with designing a control panel. You will see the panel on the bottom of the image. The look, colors, size, placement, etc. can change, but it has to remain horizontal, that's my only requirement. Overall, I'm open to suggestions. Thank you for your help!

NOTE: the last two items (success rate and progress) are indicators, not buttons, so they should look different from the buttons.

Industry/Entity Type

Learning

Other font styles liked:
• Open Sans

```html
<!DOCTYPE html>
<html lang="en">
<head>
<meta charset="utf-8">
<title>Simulation Control Panel</title>
<link href="https://fonts.googleapis.com/css2?family=Open+Sans:wght@400;600;700&display=swap" rel="stylesheet">
<style>
  :root {
    --panel-bg: #282828;
    --panel-rim: #4a4438;
    --accent: #19aee6;
    --accent-dark: #0f7fae;
    --track: #1d3947;
    --label: #e9e9e9;
    --button-face: #ffffff;
    --nav-bg: #1f1f1f;
    --nav-border: #5a5a5a;
  }
  html, body {
    margin: 0;
    padding: 0;
    width: 1200px;
    height: 675px;
    overflow: hidden;
    background: #1b2d3f;
    font-family: "Open Sans", Arial, sans-serif;
  }
  .stage {
    position: relative;
    width: 1200px;
    height: 675px;
    overflow: hidden;
  }
  .scene {
    position: absolute;
    inset: 0;
    background:
      radial-gradient(ellipse 260px 160px at 660px 260px, rgba(240,248,255,0.85), rgba(200,225,245,0) 70%),
      radial-gradient(ellipse 520px 200px at 700px 420px, rgba(230,210,120,0.55), rgba(230,210,120,0) 70%),
      radial-gradient(ellipse 420px 260px at 1150px 560px, rgba(210,170,80,0.7), rgba(210,170,80,0) 70%),
      radial-gradient(ellipse 380px 260px at 150px 420px, rgba(60,110,60,0.8), rgba(60,110,60,0) 70%),
      radial-gradient(ellipse 500px 200px at 900px 60px, rgba(40,60,140,0.9), rgba(40,60,140,0) 70%),
      linear-gradient(180deg, #8fb6de 0%, #4f7fa3 30%, #3f6a4a 60%, #8a8a4a 85%, #b08a4e 100%);
  }
  .alert-pin {
    position: absolute;
    left: 490px;
    top: 144px;
    width: 68px;
    height: 108px;
  }
  .control-panel {
    position: absolute;
    left: 206px;
    top: 565px;
    width: 786px;
    height: 120px;
    box-sizing: border-box;
    background: var(--panel-bg);
    border: 6px solid var(--panel-rim);
    border-bottom: none;
    border-radius: 34px 34px 0 0;
  }
  .control-button {
    position: absolute;
    top: 14px;
    width: 90px;
    margin-left: -45px;
    text-align: center;
    color: var(--label);
    font-size: 11.5px;
    letter-spacing: 0.1px;
  }
  .control-button .ring {
    display: block;
    width: 60px;
    height: 60px;
    margin: 0 auto 11px;
  }
  .indicator {
    position: absolute;
    color: var(--label);
    text-align: center;
  }
  .success-rate {
    left: 566px;
    top: 12px;
    width: 124px;
    font-size: 11.5px;
  }
  .success-rate svg { display: block; margin: 0 auto; }
  .success-rate .value {
    position: absolute;
    left: 0;
    right: 0;
    top: 45px;
    font-size: 14px;
  }
  .success-rate .caption { margin-top: 8px; }
  .call-progress {
    left: 696px;
    top: 41px;
    width: 76px;
    font-size: 9.5px;
    line-height: 12px;
  }
  .pager {
    position: absolute;
    top: 650px;
    height: 20px;
    box-sizing: border-box;
    padding: 0 6px;
    line-height: 18px;
    background: var(--nav-bg);
    border: 1px solid var(--nav-border);
    border-radius: 3px;
    color: #fff;
    font-size: 11px;
    font-weight: 700;
    text-align: center;
  }
  .pager.prev { left: 1080px; width: 55px; }
  .pager.next { left: 1141px; width: 55px; }
</style>
</head>
<body>
<div class="stage">
  <div class="scene" role="img" aria-label="Dotted world map over a blurred light-streak background in blue, green and gold"></div>

  <svg class="alert-pin" viewBox="0 0 68 108" aria-label="Incident location marker">
    <defs>
      <linearGradient id="pinFill" x1="0" y1="0" x2="0" y2="1">
        <stop offset="0" stop-color="#f5c400"/>
        <stop offset="0.55" stop-color="#e8901a"/>
        <stop offset="1" stop-color="#c0521c"/>
      </linearGradient>
    </defs>
    <path d="M34 108 C26 88 2 66 2 34 A32 32 0 0 1 66 34 C66 66 42 88 34 108 Z" fill="url(#pinFill)"/>
    <circle cx="34" cy="32" r="21" fill="#fff" stroke="#f2c200" stroke-width="3"/>
    <path d="M26 41 V34 a8 8 0 0 1 16 0 V41 Z" fill="#8a2b1c"/>
    <rect x="23" y="41" width="22" height="4" fill="#8a2b1c"/>
    <g stroke="#8a2b1c" stroke-width="2" stroke-linecap="round">
      <line x1="34" y1="17" x2="34" y2="21"/>
      <line x1="24" y1="21" x2="26.5" y2="24"/>
      <line x1="44" y1="21" x2="41.5" y2="24"/>
    </g>
  </svg>

  <div class="control-panel">
    <div class="control-button" style="left:55px">
      <svg class="ring" viewBox="0 0 60 60">
        <circle cx="30" cy="30" r="29" fill="none" stroke="var(--accent)" stroke-width="2"/>
        <circle cx="30" cy="30" r="26" fill="#111"/>
        <circle cx="30" cy="30" r="22" fill="var(--button-face)"/>
        <g fill="none" stroke="var(--accent)" stroke-width="1.6">
          <circle cx="30" cy="30" r="12"/>
          <ellipse cx="30" cy="30" rx="5.5" ry="12"/>
          <line x1="18" y1="30" x2="42" y2="30"/>
          <path d="M20 23 H40 M20 37 H40"/>
        </g>
      </svg>
      MAP
    </div>
    <div class="control-button" style="left:146px">
      <svg class="ring" viewBox="0 0 60 60">
        <circle cx="30" cy="30" r="29" fill="none" stroke="var(--accent)" stroke-width="2"/>
        <circle cx="30" cy="30" r="26" fill="#111"/>
        <circle cx="30" cy="30" r="22" fill="var(--button-face)"/>
        <path d="M23 19 H35 V42 L29 36 L23 42 Z" fill="none" stroke="var(--accent)" stroke-width="1.6" stroke-linejoin="round"/>
        <circle cx="37" cy="21" r="4.5" fill="var(--accent)"/>
        <path d="M37 18.6 V23.4 M34.6 21 H39.4" stroke="#fff" stroke-width="1.4"/>
      </svg>
      BOOKMARKS
    </div>
    <div class="control-button" style="left:242px">
      <svg class="ring" viewBox="0 0 60 60">
        <circle cx="30" cy="30" r="29" fill="none" stroke="var(--accent)" stroke-width="2"/>
        <circle cx="30" cy="30" r="26" fill="#111"/>
        <circle cx="30" cy="30" r="22" fill="var(--button-face)"/>
        <g fill="#fff" stroke="var(--accent)" stroke-width="1.5">
          <rect x="29" y="18" width="11" height="15"/>
          <rect x="25" y="21" width="11" height="15"/>
          <rect x="21" y="24" width="11" height="16"/>
        </g>
        <path d="M23.5 28 H29.5 M23.5 31 H29.5 M23.5 34 H29.5 M23.5 37 H29.5" stroke="var(--accent)" stroke-width="1.2"/>
      </svg>
      CASE PROFILE
    </div>
    <div class="control-button" style="left:333px">
      <svg class="ring" viewBox="0 0 60 60">
        <circle cx="30" cy="30" r="29" fill="none" stroke="var(--accent)" stroke-width="2"/>
        <circle cx="30" cy="30" r="26" fill="#111"/>
        <circle cx="30" cy="30" r="22" fill="var(--button-face)"/>
        <path d="M33 21 H21 V40 H38 V29" fill="none" stroke="var(--accent)" stroke-width="1.6" stroke-linejoin="round"/>
        <path d="M27 33 L28 29 L38 19 L41 22 L31 32 Z" fill="none" stroke="var(--accent)" stroke-width="1.5" stroke-linejoin="round"/>
      </svg>
      NOTES
    </div>
    <div class="control-button" style="left:424px">
      <svg class="ring" viewBox="0 0 60 60">
        <circle cx="30" cy="30" r="29" fill="none" stroke="var(--accent)" stroke-width="2"/>
        <circle cx="30" cy="30" r="26" fill="#111"/>
        <circle cx="30" cy="30" r="22" fill="var(--button-face)"/>
        <rect x="19" y="23" width="22" height="15" fill="none" stroke="var(--accent)" stroke-width="1.5"/>
        <path d="M19 23 L30 32 L41 23 M19 38 L27 30 M41 38 L33 30" fill="none" stroke="var(--accent)" stroke-width="1.3"/>
      </svg>
      EMAIL
    </div>
    <div class="control-button" style="left:516px">
      <svg class="ring" viewBox="0 0 60 60">
        <circle cx="30" cy="30" r="29" fill="none" stroke="var(--accent)" stroke-width="2"/>
        <circle cx="30" cy="30" r="26" fill="#111"/>
        <circle cx="30" cy="30" r="22" fill="var(--button-face)"/>
        <path d="M26 26 h13 a4 4 0 0 1 4 4 v5 a4 4 0 0 1 -4 4 h-1 l1 4 l-5 -4 h-8 a4 4 0 0 1 -4 -4 v-5 a4 4 0 0 1 4 -4 Z" fill="var(--accent-dark)"/>
        <path d="M21 18 h14 a4 4 0 0 1 4 4 v5 a4 4 0 0 1 -4 4 h-8 l-5 4 l1 -4 h-2 a4 4 0 0 1 -4 -4 v-5 a4 4 0 0 1 4 -4 Z" fill="var(--accent)"/>
        <path d="M22 23 H34 M22 26.5 H31" stroke="#fff" stroke-width="1.4"/>
      </svg>
      CHAT
    </div>

    <div class="indicator success-rate">
      <svg width="124" height="58" viewBox="0 0 124 58">
        <path d="M10 56 A52 52 0 0 1 114 56" fill="none" stroke="var(--track)" stroke-width="14"/>
        <path d="M10 56 A52 52 0 0 1 104.1 25.4" fill="none" stroke="var(--accent)" stroke-width="14"/>
        <circle cx="104.1" cy="25.4" r="7" fill="#fff"/>
      </svg>
      <div class="value">80%</div>
      <div class="caption">SUCCESS RATE</div>
    </div>

    <div class="indicator call-progress">CALL &nbsp;X OF Y<br>PROGRESS</div>
  </div>

  <div class="pager prev">&lt; PREV</div>
  <div class="pager next">NEXT &gt;</div>
</div>
</body>
</html>
```